Ebook sucht Cover
Zielgruppe
Wir betreiben diverse Internetprojekte- und -portale aller Themen und Branchen.
Aufgabenstellung
Wir haben im März 2014 ein Ebook über die Investitionsmöglichkeiten im Irak erarbeitet, welches derzeit auf aktuellen von Herbst 2015 Stand gebracht und überarbeitet wird. Vor Einfall der KV, war der Irak, vorrangig die Region Kurdistan, Erbil, ein sehr beliebtes Investitionsziel. Unser Ebook erzählt die Geschichte, Zahlen, Daten Fakten, aktuelle Situation sowie Zukunftsaussichten für ein Land (vor dem KV) mit einem des mit weltweit größten Wirtschaftswachstums.
Titel: Goldene Brücken - Traum oder Wende-Zeit
Format A4
kein Verlagslogo- und Autor auf Titelseite

```html
<!DOCTYPE html>
<html lang="de">
<head>
<meta charset="utf-8">
<title>Goldene Brücken – Traum oder Wende-Zeit</title>
<link href="https://fonts.googleapis.com/css2?family=Arimo:wght@700&display=swap" rel="stylesheet">
<style>
  :root {
    --sand-dark: #d2ba8d;
    --sand-mid: #dacaa8;
    --sand-light: #ddcfb1;
    --title-white: #ffffff;
    --rule-white: #f3f0f1;
    --accent-gold: #cca96a;
    --shadow: rgba(70, 55, 35, 0.75);
  }
  html, body {
    margin: 0;
    padding: 0;
    overflow: hidden;
  }
  .cover {
    position: relative;
    width: 848px;
    height: 1200px;
    overflow: hidden;
    background: var(--sand-dark);
    font-family: "Arimo", Arial, sans-serif;
    font-weight: 700;
  }
  .backdrop {
    position: absolute;
    inset: 0;
  }
  .title-line {
    position: absolute;
    left: 54px;
    margin: 0;
    font-size: 136px;
    line-height: 1;
    letter-spacing: -2px;
    color: var(--title-white);
    text-shadow: 3px 4px 4px var(--shadow);
    white-space: nowrap;
  }
  .title-line--first { top: 212px; }
  .title-line--second { top: 368px; }
  .title-rule {
    position: absolute;
    left: 48px;
    top: 347px;
    width: 765px;
    height: 16px;
    background: linear-gradient(var(--title-white), var(--rule-white) 60%, #e6e1e3);
    box-shadow: 2px 3px 4px var(--shadow);
  }
  .subtitle-line {
    position: absolute;
    left: 76px;
    margin: 0;
    font-size: 107px;
    line-height: 1;
    letter-spacing: -1px;
    color: var(--accent-gold);
    text-shadow: 2px 3px 4px rgba(90, 70, 40, 0.6);
    white-space: nowrap;
  }
  .subtitle-line--first { top: 776px; }
  .subtitle-line--second { top: 904px; }
</style>
</head>
<body>
  <main class="cover">
    <svg class="backdrop" width="848" height="1200" viewBox="0 0 848 1200" aria-hidden="true">
      <path d="M0 187 C130 140 260 128 370 128 C560 128 660 160 740 205 C790 232 825 262 848 290 L848 1200 L0 1200 Z" fill="var(--sand-mid)"/>
      <path d="M0 567 C100 480 230 426 366 426 C520 426 620 480 690 560 C760 640 810 720 848 805 L848 1200 L0 1200 Z" fill="var(--sand-light)"/>
    </svg>

    <h1 class="title">
      <span class="title-line title-line--first">GOLDENE</span>
      <span class="title-rule"></span>
      <span class="title-line title-line--second">BRÜCKEN</span>
    </h1>

    <p class="subtitle">
      <span class="subtitle-line subtitle-line--first">Traum oder</span>
      <span class="subtitle-line subtitle-line--second">Wende-Zeit</span>
    </p>
  </main>
</body>
</html>
```